Label design

Description
I want you to design a label for a skin care product line. I’ve provide the picture of the jar we are using along with the logo. Please note that the logo is available in different colors as well. (See attached) I would like the label to be very clean and straight to the point. Here is some info that I would like to see on the label:
240G
Net wt 8.0z

The content of the jar can be refer to as:

Body cream
Crème de corps
Body butter
Fade cream
Skin tone cream
Lotion pour le corps
Clarifying Body cream
Lightening Cream

The content is also made an exotic component that: “Extraits de noisette de palmiers” meaning nuts extract.

The brand NAME is: Miravé
The tag line is: Care for the skin you live in

Industry/Entity Type

Skin Care Product

```html
<!DOCTYPE html>
<html lang="fr">
<head>
<meta charset="utf-8">
<title>Miravé — Crème de corps label</title>
<link rel="stylesheet" href="https://fonts.googleapis.com/css2?family=Quicksand:wght@400;600&display=swap">
<style>
  :root {
    --page-bg: #eef1f3;
    --label-bg: #ffffff;
    --label-edge: #c9d3d8;
    --brand-ink: #e8641b;
    --tag-ink: #f26f21;
    --arc-start: #ffab00;
    --arc-end: #ff5500;
    --arc-text: #ffffff;
  }
  * { margin: 0; padding: 0; box-sizing: border-box; }
  html, body {
    width: 926px;
    height: 1200px;
    overflow: hidden;
    background: var(--page-bg);
  }
  .canvas {
    position: relative;
    width: 926px;
    height: 1200px;
  }
  .label {
    position: absolute;
    left: 53px;
    top: 285px;
    width: 820px;
    height: 630px;
    background: var(--label-bg);
    border: 1px solid var(--label-edge);
    border-radius: 8px;
    overflow: hidden;
  }
  .label__arc {
    position: absolute;
    left: 0;
    top: 0;
    width: 820px;
    height: 630px;
  }
  .arc-stop--start { stop-color: var(--arc-start); }
  .arc-stop--end { stop-color: var(--arc-end); }
  .brand-name {
    position: absolute;
    left: 0;
    right: 0;
    top: 205px;
    text-align: center;
    font-family: "Quicksand", sans-serif;
    font-weight: 600;
    font-size: 84px;
    line-height: 1;
    letter-spacing: 2px;
    color: var(--brand-ink);
  }
  .tagline {
    position: absolute;
    left: 0;
    right: 0;
    top: 322px;
    text-align: center;
    font-family: "Quicksand", sans-serif;
    font-weight: 400;
    font-size: 27px;
    line-height: 1.2;
    color: var(--tag-ink);
  }
  .product-name {
    position: absolute;
    left: 0;
    right: 0;
    top: 482px;
    text-align: center;
    font-family: "Quicksand", sans-serif;
    font-weight: 400;
    font-size: 44px;
    line-height: 1.2;
    color: var(--arc-text);
  }
  .net-weight {
    position: absolute;
    left: 0;
    right: 0;
    top: 560px;
    text-align: center;
    font-family: "Quicksand", sans-serif;
    font-weight: 400;
    font-size: 33px;
    line-height: 1.2;
    color: var(--arc-text);
  }
</style>
</head>
<body>
  <main class="canvas">
    <section class="label">
      <svg class="label__arc" viewBox="0 0 820 630" aria-hidden="true">
        <defs>
          <linearGradient id="arcFill" x1="0" y1="0" x2="1" y2="0">
            <stop class="arc-stop--start" offset="0"/>
            <stop class="arc-stop--end" offset="1"/>
          </linearGradient>
        </defs>
        <path d="M18 630 Q410 260 802 630 Z" fill="url(#arcFill)"/>
      </svg>
      <h1 class="brand-name">Miravé</h1>
      <p class="tagline">Care for the skin you live in</p>
      <p class="product-name">Crème de corps</p>
      <p class="net-weight">Net wt 8.0z</p>
    </section>
  </main>
</body>
</html>
```